Business Cards & Stationary Levy Appeal Counsel Partners
Business Cards & Stationary
Business Cards & Stationary Levy Appeal Counsel Partners  - Law
Creative Brief
Professional
Nora Bastable
Attorney
27480 Heron Bluff Boulevard, #200 Leawood, Kansas 66389
nbastable@lacp-mail.net
LACP-mail.net
The card will need to have our logo on it and the tag line: Member, National Assessment Dispute Alliance

```html
<!DOCTYPE html>
<html lang="en">
<head>
<meta charset="utf-8">
<title>Levy Appeal Counsel Partners – Stationery</title>
<link href="https://fonts.googleapis.com/css2?family=Libre+Baskerville&family=Arimo&display=swap" rel="stylesheet">
<style>
:root{
  --ink:#2b2b2b;
  --paper:#ffffff;
  --canvas:#f2f2f2;
  --edge:#b9b9b9;
  --night:#0d0f14;
  --glow:#3a8fd8;
  --glow-soft:#9fcdf2;
  --ghost:#ededed;
  --steel:#6f6f6f;
}
*{box-sizing:border-box;margin:0;padding:0}
html,body{width:1200px;height:919px;overflow:hidden;background:var(--canvas)}
body{position:relative;font-family:'Libre Baskerville',serif;color:var(--ink)}
.sheet{position:absolute;background:var(--paper);border:1px solid var(--edge);overflow:hidden}
.letterhead-a{left:30px;top:25px;width:480px;height:553px}
.letterhead-b{left:515px;top:25px;width:443px;height:553px}
.top-band{position:absolute;left:0;top:0;right:0;height:14px;
  background:linear-gradient(90deg,var(--night) 0%,#1b2a3e 30%,var(--glow-soft) 50%,#1b2a3e 70%,var(--night) 100%)}
.wordmark{position:absolute;font-family:'Libre Baskerville',serif;color:var(--ink);line-height:1.05;letter-spacing:.5px}
.wordmark .short{display:block;font-size:34px;letter-spacing:4px}
.wordmark .long{display:block;font-size:9px;letter-spacing:1px;margin-top:3px;text-transform:uppercase}
.ghost-mark{position:absolute;font-family:'Libre Baskerville',serif;color:var(--ghost);font-size:80px;line-height:1;letter-spacing:2px;white-space:nowrap}
.small-print{position:absolute;font-family:'Arimo',sans-serif;font-size:6px;line-height:9px;color:var(--steel);white-space:nowrap}
.card{position:absolute;left:976px;width:199px;height:101px;border:1px solid var(--edge);overflow:hidden;background:var(--paper)}
.card.dark{top:25px;background:linear-gradient(90deg,var(--night),#1a1f29 60%,#2d3544)}
.card.plain{top:145px}
.card.logo{top:264px}
.card.blue{top:386px;background:radial-gradient(ellipse at 50% 60%,var(--glow-soft) 0%,var(--glow) 35%,#0f2d52 80%)}
.card.grey{top:505px;background:linear-gradient(90deg,#555 0%,#cfcfcf 50%,#555 100%)}
.card .wordmark .short{font-size:22px;letter-spacing:3px}
.card .wordmark .long{font-size:5px;letter-spacing:.6px}
.card .wordmark.centered{left:0;right:0;top:30px;text-align:center}
.card.dark .wordmark,.card.dark .small-print{color:#e6e6e6}
.envelope{position:absolute;top:612px;height:284px;background:var(--paper);border:1px solid var(--edge);overflow:hidden}
.envelope-a{left:45px;width:473px}
.envelope-b{left:647px;width:498px}
.flap{position:absolute;left:0;right:0;top:0;height:66px;border-radius:14px 14px 0 0}
.envelope-a .flap{background:linear-gradient(90deg,var(--night) 0%,#143459 35%,var(--glow-soft) 50%,#143459 65%,var(--night) 100%)}
.envelope-b .flap{background:linear-gradient(90deg,#1a1a1a 0%,#555 35%,#e8e8e8 50%,#555 65%,#1a1a1a 100%)}
.flap-dot{position:absolute;top:22px;width:22px;height:22px;border:2px solid rgba(255,255,255,.8)}
</style>
</head>
<body>

<section class="sheet letterhead-a">
  <div class="top-band"></div>
  <div class="wordmark" style="left:26px;top:30px"><span class="short">LACP</span><span class="long">Levy Appeal Counsel Partners</span></div>
  <div class="ghost-mark" style="left:200px;top:380px">LACP</div>
  <p class="small-print" style="left:20px;top:510px">27480 Heron Bluff Boulevard, #200 · Leawood, Kansas 66389<br>Tel 913.555.0142 · LACP-mail.net<br>nbastable@lacp-mail.net</p>
</section>

<section class="sheet letterhead-b">
  <div class="wordmark" style="left:24px;top:28px"><span class="short">LACP</span><span class="long">Levy Appeal Counsel Partners</span></div>
  <p class="small-print" style="left:250px;top:26px">27480 Heron Bluff Boulevard, #200<br>Leawood, Kansas 66389 · LACP-mail.net<br>nbastable@lacp-mail.net</p>
  <div class="ghost-mark" style="left:170px;top:380px">LACP</div>
</section>

<div class="card dark">
  <div class="wordmark" style="left:10px;top:12px"><span class="short">LACP</span><span class="long">Levy Appeal Counsel Partners</span></div>
  <p class="small-print" style="left:10px;top:62px">Nora Bastable, Attorney<br>Member, National Assessment Dispute Alliance</p>
</div>
<div class="card plain">
  <p class="small-print" style="left:12px;top:16px">Nora Bastable · Attorney<br>27480 Heron Bluff Boulevard, #200<br>Leawood, Kansas 66389<br>nbastable@lacp-mail.net</p>
</div>
<div class="card logo">
  <div class="wordmark centered"><span class="short">LACP</span><span class="long">Levy Appeal Counsel Partners</span></div>
</div>
<div class="card blue">
  <div class="wordmark centered" style="color:#0a1422"><span class="short">LACP</span><span class="long">Levy Appeal Counsel Partners</span></div>
</div>
<div class="card grey">
  <div class="wordmark centered" style="color:#1d1d1d"><span class="short">LACP</span><span class="long">Levy Appeal Counsel Partners</span></div>
</div>

<section class="envelope envelope-a">
  <div class="flap"><span class="flap-dot" style="left:225px"></span></div>
  <div class="wordmark" style="left:10px;top:78px"><span class="short">LACP</span><span class="long">Levy Appeal Counsel Partners</span></div>
  <p class="small-print" style="left:10px;top:140px">27480 Heron Bluff Boulevard, #200<br>Leawood, Kansas 66389</p>
  <div class="ghost-mark" style="left:200px;top:190px">LACP</div>
</section>

<section class="envelope envelope-b">
  <div class="flap"><span class="flap-dot" style="left:238px"></span></div>
  <div class="wordmark" style="left:10px;top:78px"><span class="short">LACP</span><span class="long">Levy Appeal Counsel Partners</span></div>
  <p class="small-print" style="left:10px;top:140px">27480 Heron Bluff Boulevard, #200<br>Leawood, Kansas 66389</p>
  <div class="ghost-mark" style="left:220px;top:190px">LACP</div>
</section>

</body>
</html>
```